A Speech Therapy Business needs to update their logo

I need an update to the font and color of my logo to look more appealing. I am looking to open a private practice as a Speech Language Pathologist that caters to adults and children. It needs to be sophisticated and friendly at the same time. I want to keep the silhouette in my logo as is, just update the font and color for "Brightpaths".
Industry/Entity Type
Business
Contact Information for Business Card
I want the business card to have my logo, my name (Dorota Valk, CCC-SLP, TSSLD) and that I am a Bilingual Speech Language Pathologist. Also, include my phone number, (555) 271-8390. Include my website, Brightpathsslp.example, and email address, dorotavalk@brightpathsslp.example
Look and feel
Each slider illustrates characteristics of the customer's brand and the style your logo design should communicate.

```html
<!DOCTYPE html>
<html lang="en">
<head>
<meta charset="utf-8">
<title>Brightpaths Business Card</title>
<link href="https://fonts.googleapis.com/css2?family=Arimo:wght@400&display=swap" rel="stylesheet">
<style>
  :root {
    --page-bg: #2b2d31;
    --card-white: #ffffff;
    --bubble-grey: #f0f0f0;
    --band-grey: #5c5c5c;
    --brand-green: #237244;
    --text-grey: #6a6a6a;
    --wordmark-dark: #3a3a3a;
    --icon-grey: #5f5f5f;
    --silhouette-dark: #2a2a2a;
  }
  * { box-sizing: border-box; margin: 0; padding: 0; }
  html, body {
    width: 1200px; height: 900px; overflow: hidden;
    background: var(--page-bg);
    font-family: "Arimo", Arial, sans-serif;
  }
  .card {
    position: absolute; left: 100px; top: 164px;
    width: 1000px; height: 572px;
    background: var(--card-white);
    overflow: hidden;
  }
  .speech-bubble { position: absolute; left: 0; top: 0; width: 1000px; height: 362px; }
  .identity { position: absolute; left: 62px; top: 82px; }
  .identity__name {
    color: var(--brand-green); font-size: 44px; font-weight: 400; line-height: 1;
  }
  .identity__credentials {
    margin-top: 14px; color: var(--text-grey); font-size: 20px; line-height: 1.2;
  }
  .identity__website {
    display: flex; align-items: center; gap: 16px;
    margin-top: 40px; color: var(--text-grey); font-size: 30px;
  }
  .identity__website svg { width: 34px; height: 34px; }
  .brand { position: absolute; left: 560px; top: 62px; width: 400px; }
  .brand__silhouette {
    width: 380px; height: 120px; margin-left: 10px;
    background: linear-gradient(90deg, var(--silhouette-dark), #4a4a4a);
    border-radius: 6px;
  }
  .brand__name {
    margin-top: 22px; text-align: center;
    color: var(--wordmark-dark); font-size: 52px; font-weight: 400;
    line-height: 1;
  }
  .band { position: absolute; left: 0; width: 100%; display: flex; justify-content: center; color: #fff; }
  .band--phone {
    top: 362px; height: 72px; background: var(--band-grey);
    align-items: center; font-size: 30px; gap: 20px;
  }
  .band--email {
    top: 434px; height: 138px; background: var(--brand-green);
    padding-top: 30px; font-size: 31px; gap: 20px;
  }
  .band svg { width: 30px; height: 30px; flex: none; }
  .band--email svg { margin-top: 4px; }
</style>
</head>
<body>
  <div class="card">
    <svg class="speech-bubble" viewBox="0 0 1000 362" aria-hidden="true">
      <path d="M0 0 H470 C440 90 448 160 480 200 L548 252 L468 240 C430 290 385 330 330 362 H0 Z" fill="var(--bubble-grey)"/>
    </svg>

    <div class="identity">
      <h1 class="identity__name">Dorota Valk</h1>
      <p class="identity__credentials">CCC-SLP, TSSLD<br>Bilingual Speech Language Pathologist</p>
      <p class="identity__website">
        <svg viewBox="0 0 24 24" aria-hidden="true">
          <circle cx="12" cy="12" r="11" fill="var(--icon-grey)"/>
          <path d="M6 7c2 0 3 1 3 3s-2 2-2 4 1 3 0 5c-2-1-4-4-4-7 0-2 1-4 3-5zM14 4c2 1 1 3 3 3s2 2 2 4-2 1-3 3 0 4-2 5c-1-2 0-3-1-5s-3-1-3-3 3-2 3-4-1-2 1-3z" fill="#fff"/>
        </svg>
        brightpathsslp.example
      </p>
    </div>

    <div class="brand">
      <div class="brand__silhouette" role="img" aria-label="Silhouette of a row of children and adults holding hands, ending in a small heart"></div>
      <p class="brand__name">Brightpaths</p>
    </div>

    <div class="band band--phone">
      <svg viewBox="0 0 24 24" aria-hidden="true">
        <path d="M6.6 10.8c1.4 2.8 3.8 5.1 6.6 6.6l2.2-2.2c.3-.3.7-.4 1-.2 1.1.4 2.3.6 3.6.6.6 0 1 .4 1 1V20c0 .6-.4 1-1 1C10.6 21 3 13.4 3 4c0-.6.4-1 1-1h3.5c.6 0 1 .4 1 1 0 1.3.2 2.5.6 3.6.1.3 0 .7-.2 1z" fill="#fff"/>
      </svg>
      <span>(555) 271-8390</span>
    </div>

    <div class="band band--email">
      <svg viewBox="0 0 24 24" aria-hidden="true">
        <rect x="2" y="5" width="20" height="14" fill="#fff"/>
        <path d="M2 5l10 8 10-8M2 19l7-7M22 19l-7-7" stroke="var(--brand-green)" stroke-width="1.4" fill="none"/>
      </svg>
      <span>dorotavalk@brightpathsslp.example</span>
    </div>
  </div>
</body>
</html>
```